Marlowvale Wholefoods web design

Go to marlowvalewholefoods.com.au an using the current layout create a design that will attract customers to this wholefood website.

You may suggest / make slight changes to the layout to create effective graphic design principles.

The LOGO design is TM already. So no changes there. Second logo attached is authorised for use and is a area branding LOGO.

Colours need to reflect health and wellbeing.

Don't want Medical style or New age.
Updates

Thank you for your submissions so far. I have sent them out to a trusty panel of friends to hear what they have to say. Some of you have done very well.

Reason: There are a few submissions outstanding. I will eliminate a few designs today and give feed back. Thankyou

Thank you for your submissions so far I will not be asking for more design submissions from other designers. The ones I have are under consideration and there are a few minor changes to each that may just bring out the one that is IT! The two designs I have narrowed it down to are very different in approach so please bear with me a couple more days. Thank you.

Target Market(s)

Whole food health concious people target market locally Home Delivery would be young Mums with restricted movement because of young children. Older people that are restricted transport users.

Busy commuters that leave our area for work and just want to relax on the weekend with their family and local bush walking or garden activities.

Industry/Entity Type

Graphic Design

Requirements
Should not have
• Medical or sterile hospital feel. New age or too alternative living feel.

```html
<!DOCTYPE html>
<html lang="en">
<head>
<meta charset="utf-8">
<title>Marlowvale Wholefoods</title>
<link rel="stylesheet" href="https://fonts.googleapis.com/css2?family=Arimo:wght@400;700&family=Cabin:wght@400;600&family=Josefin+Sans:wght@600;700&family=Roboto+Condensed:wght@700&display=swap">
<style>
:root{
  --purple:#6b0f6b;
  --purple-dark:#4e0a4e;
  --green:#8acc0a;
  --green-bright:#45e600;
  --green-text:#6aa517;
  --ink:#222;
  --muted:#555;
  --line:#dcdcdc;
  --panel:#f7f7f7;
  --footer:#343434;
  --red:#d81919;
}
*{box-sizing:border-box;margin:0;padding:0}
html,body{width:901px;height:1200px;overflow:hidden;background:#fff}
body{position:relative;font-family:Arimo,Arial,sans-serif;color:var(--ink)}
.abs{position:absolute}
.top-rule{left:0;top:0;width:901px;height:3px;background:var(--purple)}
.account-tab{top:0;height:32px;background:var(--purple);color:#fff;font-size:12px;display:flex;align-items:center;justify-content:center;border-radius:0 0 4px 4px}
.brand{left:78px;top:22px;display:flex;align-items:center;gap:8px}
.brand-dot{width:30px;height:30px;border-radius:50%;background:var(--green)}
.brand-name{font-family:Cabin,sans-serif;font-weight:600;font-size:17px;color:var(--purple);line-height:1.1;width:110px}
.call{left:450px;top:54px;width:190px;height:28px;border-bottom:1px dotted #999;display:flex;align-items:center;gap:6px;font-family:"Roboto Condensed",sans-serif;font-size:14px}
.call-icon{width:20px;height:20px;background:#5aa02c;border-radius:2px;display:flex;align-items:center;justify-content:center}
.call-number{color:var(--green-text);font-size:16px;margin-left:4px}
.cart{left:664px;top:48px;width:158px;height:37px;border:1px solid #ccc;border-radius:4px;background:#fff;box-shadow:0 1px 3px rgba(0,0,0,.12)}
.cart-label{left:44px;top:5px;font-size:9.5px;line-height:12px;color:#333;font-weight:700}
.cart-label span{font-weight:400}
.checkout{left:98px;top:9px;width:54px;height:20px;background:var(--red);color:#fff;font-size:9px;border-radius:3px;display:flex;align-items:center;justify-content:center}
.main-nav{left:77px;top:106px;width:745px;height:29px;background:var(--green);border:1px solid #b5e35a;border-radius:2px}
.main-nav a{position:absolute;top:0;height:27px;line-height:27px;font-size:11px;color:#111;text-decoration:none;transform:translateX(-50%);white-space:nowrap}
.nav-divider{position:absolute;top:3px;width:1px;height:21px;background:#74ad06}
.hero{left:78px;top:144px;width:744px;height:275px;border:2px solid #ccc;background:#fff;overflow:hidden}
.hero-image{left:20px;top:20px;width:600px;height:240px;background:linear-gradient(100deg,#d9876a 0%,#e8c08a 25%,#4fa8d8 50%,#f2a23a 75%,#f6f3d8 100%)}
.hero-caption{left:0;top:232px;width:740px;height:39px;background:rgba(40,40,40,.88);color:#fff;font-family:"Josefin Sans",sans-serif;font-weight:700;font-size:21px;padding:10px 0 0 18px;letter-spacing:.5px}
.newsletter{left:578px;top:194px;width:211px;height:206px;background:#fff;border:1px solid #ddd;box-shadow:0 0 6px rgba(0,0,0,.15)}
.newsletter h2{position:absolute;left:17px;top:18px;font-family:"Josefin Sans",sans-serif;font-size:16.5px;color:var(--purple);font-weight:700}
.newsletter p{position:absolute;left:17px;top:42px;width:185px;font-size:9.8px;line-height:13.5px;color:#333}
.field{position:absolute;left:17px;width:173px;height:24px;border:1px solid #ccc;font-size:9px;color:#999;padding:6px 7px}
.subscribe{position:absolute;left:94px;top:167px;width:96px;height:24px;background:var(--green-bright);color:#113300;border-radius:2px;font-family:"Josefin Sans",sans-serif;font-weight:700;font-size:12.5px;display:flex;align-items:center;justify-content:center;padding-top:2px}
.sidebar{left:78px;top:438px;width:184px;height:632px;background:var(--panel);border:1px solid #e8e8e8}
.ribbon{height:28px;width:168px;color:#fff;font-family:Cabin,sans-serif;font-weight:600;font-size:13.5px;line-height:28px;padding-left:18px}
.ribbon svg{position:absolute;left:0;top:0}
.ribbon span{position:relative}
.cat-list{list-style:none;left:84px;width:169px}
.cat-list li{height:25.6px;line-height:25.6px;font-size:10.3px;padding-left:4px;border-bottom:1px solid var(--line);letter-spacing:.2px}
.cat-list li:last-child{border-bottom:none}
.content{left:288px;top:438px;width:534px;height:644px;background:#fafafa;border:1px solid #e6e6e6}
.welcome{left:302px;top:444px;font-family:Cabin,sans-serif;font-size:22.5px;color:var(--green-text)}
.intro{left:302px;top:478px;width:500px;font-size:9.2px;line-height:15px;color:#333}
.readmore{left:744px;top:558px;font-size:8.5px;font-weight:700;color:var(--purple)}
.section-title{display:flex;align-items:center;gap:6px;left:302px;width:498px;font-family:Cabin,sans-serif;font-size:20.5px;color:var(--purple)}
.section-title i{flex:1;height:3px;border-top:1px solid #ccc;border-bottom:1px solid #ccc}
.product{width:150px;height:112px;background:#fff;border:1px solid #ddd;padding:2px;box-shadow:0 4px 5px -3px rgba(0,0,0,.25)}
.product-photo{width:100%;height:100%}
.price-bar{position:absolute;left:2px;right:2px;bottom:2px;height:24px;background:rgba(40,40,40,.85);display:flex;align-items:center;justify-content:center;gap:14px;color:#fff;font-family:"Roboto Condensed",sans-serif;font-size:13px}
.footer-rule{left:0;top:1106px;width:901px;height:3px;background:var(--green)}
.footer{left:0;top:1109px;width:901px;height:91px;background:var(--footer);color:#fff}
.footer-links{left:75px;top:11px;font-size:8.5px;word-spacing:2px}
.copyright{left:75px;top:29px;font-size:9px}
.cards{left:75px;top:51px;display:flex;gap:8px}
.cards span{width:26px;height:16px;background:#8a8a8a;border-radius:2px}
.cards span.wide{width:60px;background:#6a6a6a}
.partner{left:700px;top:20px;display:flex;align-items:center;gap:6px;font-family:Cabin,sans-serif}
.partner-dot{width:14px;height:14px;border-radius:50%;background:#cfcfcf}
.partner-name{font-size:15px;color:#e0e0e0;line-height:1}
.partner-sub{left:720px;top:40px;font-size:8px;color:#e0e0e0}
</style>
</head>
<body>
<div class="abs top-rule"></div>
<div class="abs account-tab" style="left:638px;width:92px">LOGIN</div>
<div class="abs account-tab" style="left:732px;width:90px">REGISTER</div>

<div class="abs brand"><span class="brand-dot"></span><span class="brand-name">Marlowvale Wholefoods</span></div>

<div class="abs call">
  <span class="call-icon"><svg width="12" height="12" viewBox="0 0 24 24"><path fill="#fff" d="M6.6 10.8a15 15 0 0 0 6.6 6.6l2.2-2.2c.3-.3.7-.4 1-.2 1.1.4 2.3.6 3.6.6.6 0 1 .4 1 1V20c0 .6-.4 1-1 1A17 17 0 0 1 3 4c0-.6.4-1 1-1h3.5c.6 0 1 .4 1 1 0 1.3.2 2.5.6 3.6.1.3 0 .7-.2 1z"/></svg></span>
  <span>CALL US:</span><span class="call-number">1 800 555 0192</span>
</div>

<div class="abs cart">
  <svg class="abs" style="left:9px;top:8px" width="30" height="22" viewBox="0 0 30 22"><path d="M1 2h5l4 12h14l3-9H8" fill="none" stroke="#6cbf1d" stroke-width="3"/><circle cx="12" cy="19" r="2.4" fill="#6cbf1d"/><circle cx="22" cy="19" r="2.4" fill="#6cbf1d"/></svg>
  <div class="abs cart-label">MY CART:<br><span>(0 ITEMS)</span></div>
  <div class="abs checkout">CHECKOUT</div>
</div>

<nav class="abs main-nav">
  <a style="left:37px">HOME</a><span class="nav-divider" style="left:82px"></span>
  <a style="left:122px">SHOP</a><span class="nav-divider" style="left:164px"></span>
  <a style="left:252px">PURCHASE BY WEIGHT</a><span class="nav-divider" style="left:340px"></span>
  <a style="left:390px">RECIPES</a><span class="nav-divider" style="left:442px"></span>
  <a style="left:482px">BLOG</a><span class="nav-divider" style="left:525px"></span>
  <a style="left:585px">CONTACT US</a>
</nav>

<section class="abs hero">
  <div class="abs hero-image" role="img" aria-label="Row of colourful breakfast cereal boxes with bowls of cereal"></div>
  <div class="abs hero-caption">Wholefoods Company...</div>
</section>

<aside class="abs newsletter">
  <h2>Join Our Newsletter</h2>
  <p>Receive exclusive offers and new product notices delivered&nbsp; to your inbox.</p>
  <div class="field" style="top:90px">Yourname</div>
  <div class="field" style="top:126px">Youremail</div>
  <div class="subscribe">Subscribe</div>
</aside>

<aside class="abs sidebar"></aside>
<div class="abs ribbon" style="left:69px;top:445px">
  <svg width="168" height="28" viewBox="0 0 168 28"><path d="M0 4 L6 0 L6 28 L0 24Z" fill="var(--purple-dark)"/><path d="M4 0H158L168 14L158 28H4Z" fill="var(--purple)"/></svg>
  <span>Product Categories</span>
</div>
<ul class="abs cat-list" style="top:474px">
  <li>Alternative goods</li><li>Dairy Free</li><li>Gluten Free</li><li>Grocery</li><li>Health Supplements</li><li>Natural Grocer</li><li>Organic</li><li>Recipes</li><li>Seasonal</li><li>Sugar Replacements</li>
</ul>
<div class="abs ribbon" style="left:69px;top:742px">
  <svg width="168" height="28" viewBox="0 0 168 28"><path d="M0 4 L6 0 L6 28 L0 24Z" fill="var(--purple-dark)"/><path d="M4 0H158L168 14L158 28H4Z" fill="var(--purple)"/></svg>
  <span>By Weight Categories</span>
</div>
<ul class="abs cat-list" style="top:777px">
  <li>Baking</li><li>Beans &amp; Peas</li><li>Candy &amp; Sweet Treats</li><li>Cereals &amp; Granolas</li><li>Coffee &amp; Tea</li><li>Dried Fruit</li><li>Free Range Meat</li><li>Gluten Free Processed Meat</li><li>Pasture Fed Beef</li><li>Pasture Grazed Lamb</li><li>Preservative Free Meat</li>
</ul>

<main class="abs content"></main>
<h1 class="abs welcome">Welcome to Marlowvale Wholefoods Company</h1>
<p class="abs intro">Lorem ipsum dolor sit amet, consectetur adipiscing elit. Quisque dapibus accumsan orci, pretium eleifend arcu adipiscing eget. Fusce accumsan facilisis tincidunt. Phasellus tempor enim purus, vitae venenatis est. Ut imperdiet hendrerit pulvinar. Cras at tellus a enim condimentum mollis ut et tellus. Mauris dolor magna, elementum eu dictum eu, fermentum a nibh. Praesent ut dui lectus, vel lacinia sem. Praesent commodo malesuada urna, quis convallis risus dictum et. Nunc dapibus interdum libero, et semper eros auctor ac.</p>
<div class="abs readmore">Readmore...</div>

<h2 class="abs section-title" style="top:585px">Latest Deals <i></i></h2>

<div class="abs product" style="left:302px;top:630px"><div class="product-photo" role="img" aria-label="Loose rolled grain mix" style="background:linear-gradient(135deg,#b7a896,#8e7f70)"></div><div class="price-bar">Now $7.30 <svg width="18" height="14" viewBox="0 0 30 22"><path d="M1 2h5l4 12h14l3-9H8" fill="none" stroke="#6cbf1d" stroke-width="3.5"/><circle cx="12" cy="19" r="2.6" fill="#6cbf1d"/><circle cx="22" cy="19" r="2.6" fill="#6cbf1d"/></svg></div></div>
<div class="abs product" style="left:477px;top:630px"><div class="product-photo" role="img" aria-label="Jar of digestive supplement on white" style="background:radial-gradient(circle at 50% 45%,#8a6a5a 0 18%,#fff 22%)"></div><div class="price-bar">Now $7.30 <svg width="18" height="14" viewBox="0 0 30 22"><path d="M1 2h5l4 12h14l3-9H8" fill="none" stroke="#6cbf1d" stroke-width="3.5"/><circle cx="12" cy="19" r="2.6" fill="#6cbf1d"/><circle cx="22" cy="19" r="2.6" fill="#6cbf1d"/></svg></div></div>
<div class="abs product" style="left:650px;top:630px"><div class="product-photo" role="img" aria-label="Pile of raw almonds" style="background:linear-gradient(135deg,#b7825a,#8a5a38)"></div><div class="price-bar">Now $7.30 <svg width="18" height="14" viewBox="0 0 30 22"><path d="M1 2h5l4 12h14l3-9H8" fill="none" stroke="#6cbf1d" stroke-width="3.5"/><circle cx="12" cy="19" r="2.6" fill="#6cbf1d"/><circle cx="22" cy="19" r="2.6" fill="#6cbf1d"/></svg></div></div>

<div class="abs product" style="left:302px;top:773px"><div class="product-photo" role="img" aria-label="Black and white grocery shelves stocked with produce" style="background:linear-gradient(135deg,#8a8a8a,#3a3a3a)"></div><div class="price-bar">Now $7.30 <svg width="18" height="14" viewBox="0 0 30 22"><path d="M1 2h5l4 12h14l3-9H8" fill="none" stroke="#6cbf1d" stroke-width="3.5"/><circle cx="12" cy="19" r="2.6" fill="#6cbf1d"/><circle cx="22" cy="19" r="2.6" fill="#6cbf1d"/></svg></div></div>
<div class="abs product" style="left:477px;top:773px"><div class="product-photo" role="img" aria-label="Bowl of coconut coated bliss balls" style="background:radial-gradient(circle,#6a4a38,#a05a2a)"></div><div class="price-bar">Now $7.30 <svg width="18" height="14" viewBox="0 0 30 22"><path d="M1 2h5l4 12h14l3-9H8" fill="none" stroke="#6cbf1d" stroke-width="3.5"/><circle cx="12" cy="19" r="2.6" fill="#6cbf1d"/><circle cx="22" cy="19" r="2.6" fill="#6cbf1d"/></svg></div></div>
<div class="abs product" style="left:650px;top:773px"><div class="product-photo" role="img" aria-label="Loose hulled seeds" style="background:linear-gradient(135deg,#a89a78,#7e7058)"></div><div class="price-bar">Now $7.30 <svg width="18" height="14" viewBox="0 0 30 22"><path d="M1 2h5l4 12h14l3-9H8" fill="none" stroke="#6cbf1d" stroke-width="3.5"/><circle cx="12" cy="19" r="2.6" fill="#6cbf1d"/><circle cx="22" cy="19" r="2.6" fill="#6cbf1d"/></svg></div></div>

<h2 class="abs section-title" style="top:904px">Latest News <i></i></h2>

<div class="abs product" style="left:302px;top:952px"><div class="product-photo" role="img" aria-label="Loose rolled grain mix" style="background:linear-gradient(135deg,#b7a896,#8e7f70)"></div><div class="price-bar">Now $7.30 <svg width="18" height="14" viewBox="0 0 30 22"><path d="M1 2h5l4 12h14l3-9H8" fill="none" stroke="#6cbf1d" stroke-width="3.5"/><circle cx="12" cy="19" r="2.6" fill="#6cbf1d"/><circle cx="22" cy="19" r="2.6" fill="#6cbf1d"/></svg></div></div>
<div class="abs product" style="left:477px;top:952px"><div class="product-photo" role="img" aria-label="Jar of digestive supplement on white" style="background:radial-gradient(circle at 50% 45%,#8a6a5a 0 18%,#fff 22%)"></div><div class="price-bar">Now $7.30 <svg width="18" height="14" viewBox="0 0 30 22"><path d="M1 2h5l4 12h14l3-9H8" fill="none" stroke="#6cbf1d" stroke-width="3.5"/><circle cx="12" cy="19" r="2.6" fill="#6cbf1d"/><circle cx="22" cy="19" r="2.6" fill="#6cbf1d"/></svg></div></div>
<div class="abs product" style="left:650px;top:952px"><div class="product-photo" role="img" aria-label="Pile of raw almonds" style="background:linear-gradient(135deg,#b7825a,#8a5a38)"></div><div class="price-bar">Now $7.30 <svg width="18" height="14" viewBox="0 0 30 22"><path d="M1 2h5l4 12h14l3-9H8" fill="none" stroke="#6cbf1d" stroke-width="3.5"/><circle cx="12" cy="19" r="2.6" fill="#6cbf1d"/><circle cx="22" cy="19" r="2.6" fill="#6cbf1d"/></svg></div></div>

<div class="abs footer-rule"></div>
<footer class="abs footer">
  <div class="abs footer-links">HOME &nbsp;| SHOP &nbsp;| PURCHASE BY WEIGHT &nbsp;| RECIPES &nbsp;| BLOG &nbsp;| CONTACT US</div>
  <div class="abs copyright">© 2014 Marlowvale Wholefoods Company.&nbsp; All rights reserved.&nbsp; Privacy Policy&nbsp; |&nbsp; Terms of Use</div>
  <div class="abs cards"><span></span><span></span><span></span><span></span><span></span><span class="wide"></span></div>
  <div class="abs partner"><span class="partner-dot"></span><span class="partner-name">Ridgeline</span></div>
  <div class="abs partner-sub">Sustainable Business</div>
</footer>
</body>
</html>
```